Copyright Registration Service Website

Rightsbloomery.com (site can be accessed) is a website that will enable artists, photographers, writers, sculptors, musicians and other creative persons of all media to register their works of authorship with the U.S. Hall of Registers, Filing Bureau, for a nominal fee of $99 plus filing fees (in most cases). The high points of marketing are (1) every application is reviewed by a lawyer and (2) the entire copyright process is monitored, as part of the service fee. There are 8 categories of copyrightability:
Literary Works
Dramatic Works
Musical Works
Sound Recordings
Motion Pictures
Choreographic and Pantomime Works
Photographs, Paintings and Sculptures
Architectural Works
Please look at the existing site; provide a better landing page than currently exists. In particular, the logo is in need of serious improvement. We would like it to be bright and sunny; visually pleasant and witty; and clever but not "doctoral" in presentation. Thank you for your participation.

Target Market(s)

photographers, artists, musicians, age groups of 20-50

Industry/Entity Type

Marketing

Requirements
Should not have
• stiffness

```html
<!DOCTYPE html>
<html lang="en">
<head>
<meta charset="utf-8">
<title>Rightsbloomery.com – Copyright Registration</title>
<link href="https://fonts.googleapis.com/css2?family=Open+Sans:wght@400;600;700&family=Patrick+Hand&family=Cinzel:wght@400&display=swap" rel="stylesheet">
<style>
:root{
  --topbar:#393e49;
  --footer:#30353f;
  --blue:#3f8be0;
  --green:#7db53b;
  --ink:#333;
  --body:#5a5a5a;
  --rule:#e2e2e2;
  --soft:#f5f5f5;
  --icon-bg:#e9e9e9;
}
*{margin:0;padding:0;box-sizing:border-box}
html,body{width:851px;height:1200px;overflow:hidden;background:#fff}
body{font-family:"Open Sans",Arial,sans-serif;color:var(--ink)}
.page{position:relative;width:851px;height:1200px;overflow:hidden}
.abs{position:absolute}

.topbar{left:0;top:0;width:851px;height:22px;background:var(--topbar)}
.social{right:80px;top:6px;display:flex;gap:7px}
.social span{width:9px;height:9px;background:#8a909b;border-radius:2px;display:block}

.header{left:0;top:22px;width:851px;height:68px;background:#fff}
.brand{left:80px;top:14px;display:flex;align-items:center;gap:7px}
.brand-mark{width:36px;height:36px;border:2px solid #222;border-radius:50%}
.brand-name{font-weight:700;font-size:14px;color:#222;letter-spacing:.3px}
.nav{right:80px;top:31px;display:flex;gap:19px;font-size:8.6px;text-transform:uppercase}
.nav a{color:#333;text-decoration:none}
.nav a.active{color:var(--blue);text-decoration:underline}

.hero{left:0;top:90px;width:851px;height:296px;
  background:radial-gradient(circle at 52% 48%,#e9b45e 0,#6f5a55 9%,transparent 24%),
  linear-gradient(90deg,transparent 60%,rgba(30,30,40,.55) 75%,rgba(30,30,40,.35) 88%,transparent 100%),
  linear-gradient(180deg,#1d2a52 0%,#34395b 45%,#5a4a4f 75%,#3b3136 100%)}
.hero-kicker{left:128px;top:61px;font-family:"Patrick Hand",cursive;font-size:17px;color:#fff;letter-spacing:.4px}
.hero-title{left:124px;top:86px;font-family:"Cinzel",serif;font-size:53px;line-height:66px;color:#fff;letter-spacing:1px}
.hero-price{left:155px;top:146px;font-family:"Patrick Hand",cursive;font-size:17px;color:#fff;letter-spacing:.4px}
.hero-sub{left:101px;top:171px;font-size:17px;color:#fff}
.hero-btn{left:208px;top:216px;width:151px;height:35px;border:1px solid #ddd;background:rgba(255,255,255,.35);
  font-size:17px;color:#333;display:flex;align-items:center;justify-content:center}
.hero-arrow{top:122px;width:38px;height:53px;background:rgba(255,255,255,.25);display:flex;align-items:center;justify-content:center}
.hero-arrow.prev{left:0}.hero-arrow.next{right:0}
.dots{left:410px;top:278px;display:flex;gap:6px}
.dots span{width:6px;height:6px;border-radius:50%;background:rgba(255,255,255,.5)}
.dots span.on{background:#fff}

.section-title{display:flex;align-items:center;gap:22px;color:var(--blue);font-weight:400;text-transform:uppercase}
.section-title::before,.section-title::after{content:"";flex:1;height:1px;background:var(--rule)}

.about{left:0;top:386px;width:851px;height:132px;background:#fff}
.about .section-title{position:absolute;left:80px;top:30px;width:691px;font-size:19px}
.about p{position:absolute;left:120px;top:65px;width:611px;text-align:center;font-size:10px;line-height:16px;color:var(--body)}

.categories{left:0;top:518px;width:851px;height:381px;background:var(--soft)}
.categories .section-title{position:absolute;left:80px;top:25px;width:691px;font-size:19px}
.tile{width:160px;height:130px}
.tile-img{position:absolute;inset:0}
.tile-cap{position:absolute;left:0;bottom:0;width:100%;height:39px;background:rgba(190,190,190,.75);
  display:flex;align-items:center;justify-content:center;text-align:center;font-weight:600;font-size:13px;line-height:16px;color:#1e1e1e}

.features{left:0;top:899px;width:851px;height:269px;background:#fff}
.features h2{position:absolute;left:0;top:30px;width:851px;text-align:center;font-weight:400;font-size:13.6px;line-height:18px;color:var(--blue)}
.feature{top:93px;width:226px;text-align:center}
.feature-icon{width:45px;height:45px;border-radius:50%;background:var(--icon-bg);border:1px solid #d3d3d3;margin:0 auto;display:flex;align-items:center;justify-content:center}
.feature h3{margin-top:17px;font-size:10px;font-weight:600;color:var(--green);text-transform:uppercase}
.feature p{margin-top:9px;font-size:8.4px;line-height:13px;color:var(--body)}

.footer{left:0;top:1168px;width:851px;height:32px;background:var(--footer)}
.footer-links{left:80px;top:10px;font-size:8.6px;color:#fff;display:flex;gap:12px}
.footer-copy{right:80px;top:11px;font-size:7.5px;color:#fff}
</style>
</head>
<body>
<div class="page">

  <div class="abs topbar">
    <div class="abs social"><span></span><span></span><span></span><span></span><span></span><span></span><span></span><span></span></div>
  </div>

  <header class="abs header">
    <div class="abs brand">
      <span class="brand-mark"></span>
      <span class="brand-name">RIGHTSBLOOMERY</span>
    </div>
    <nav class="abs nav">
      <a class="active" href="#">About Us</a>
      <a href="#">Copyright Cateogries</a>
      <a href="#">Law &amp; Statutes</a>
      <a href="#">Copyright Process</a>
      <a href="#">Contact Us</a>
      <a href="#">Links</a>
    </nav>
  </header>

  <section class="abs hero" role="img" aria-label="Evening photo of an old town square with a lit clock tower and street lamp, a young man in a dark suit with arms crossed on the right">
    <div class="abs hero-kicker">PROTECT YOUR COPYRIGHT IN 5 MINUTES!</div>
    <div class="abs hero-title">COPYRIGHT</div>
    <div class="abs hero-price">REGISTRATION $99 (MOST CASES)</div>
    <div class="abs hero-sub">ENTIRE PROCESS IS REVIEWED BY A LAWYER</div>
    <div class="abs hero-btn">LEARN MORE</div>
    <div class="abs hero-arrow prev"><svg width="16" height="30"><path d="M14 1 2 15l12 14" fill="none" stroke="#ccc" stroke-width="1.2"/></svg></div>
    <div class="abs hero-arrow next"><svg width="16" height="30"><path d="M2 1l12 14L2 29" fill="none" stroke="#ccc" stroke-width="1.2"/></svg></div>
    <div class="abs dots"><span class="on"></span><span></span><span></span></div>
  </section>

  <section class="abs about">
    <h2 class="section-title">About Us</h2>
    <p>Lorem Ipsum is simply dummy text of the printing and typesetting industry. Lorem Ipsum has been the industry's standard dummy text ever since the 1500s, when an unknown printer took a galley of type and scrambled it to make a type specimen book.</p>
  </section>

  <section class="abs categories">
    <h2 class="section-title">Categories of Copyrightability</h2>

    <div class="abs tile" style="left:80px;top:72px">
      <div class="tile-img" role="img" aria-label="Row of old leather-bound books" style="background:linear-gradient(180deg,#2a1c14,#7a5238 55%,#c4a27d)"></div>
      <div class="tile-cap">Literary Works</div>
    </div>
    <div class="abs tile" style="left:257px;top:72px">
      <div class="tile-img" role="img" aria-label="Golden theatre masks on black" style="background:radial-gradient(circle at 50% 40%,#c9a21c 0,#8a6c10 35%,#000 70%)"></div>
      <div class="tile-cap">Dramatic Works</div>
    </div>
    <div class="abs tile" style="left:434px;top:72px">
      <div class="tile-img" role="img" aria-label="Drum kit with cymbal" style="background:linear-gradient(180deg,#5a2238,#222 45%,#6b6250 80%,#333)"></div>
      <div class="tile-cap">Musical Works</div>
    </div>
    <div class="abs tile" style="left:612px;top:72px">
      <div class="tile-img" role="img" aria-label="Woman listening on studio headphones" style="background:linear-gradient(90deg,#3a3a3a,#d8b598 45%,#f0e37a)"></div>
      <div class="tile-cap">Sound Recordings</div>
    </div>

    <div class="abs tile" style="left:80px;top:218px">
      <div class="tile-img" role="img" aria-label="Dancer spinning a hoop in motion blur" style="background:radial-gradient(circle at 50% 60%,#9aa0a8 0,#3a3e48 30%,#050608 65%)"></div>
      <div class="tile-cap">Motion Pictures</div>
    </div>
    <div class="abs tile" style="left:257px;top:218px">
      <div class="tile-img" role="img" aria-label="Ballet performers on a lit stage" style="background:linear-gradient(180deg,#3a1d4a,#8a3c6a 50%,#e8a0b8)"></div>
      <div class="tile-cap">Choreographic and<br>Pantomime Works</div>
    </div>
    <div class="abs tile" style="left:434px;top:218px">
      <div class="tile-img" role="img" aria-label="Gallery of old paintings and sculptures" style="background:linear-gradient(180deg,#3a2e1a,#8c7240 50%,#4a3a22)"></div>
      <div class="tile-cap">Photographs, Paintings<br>and Sculptures</div>
    </div>
    <div class="abs tile" style="left:612px;top:218px">
      <div class="tile-img" role="img" aria-label="Modern interior with chandelier" style="background:linear-gradient(180deg,#222,#3e3a48 50%,#b9b4a8)"></div>
      <div class="tile-cap">Architectural Works</div>
    </div>
  </section>

  <section class="abs features">
    <h2>EVERY APPLICATION IS INDIVIDUALLY FILED AND MONITORED UNDER LAWYER SUPERVISION.<br>PROTECT YOUR INTELLECTUAL PROPERTY RIGHTS</h2>

    <div class="abs feature" style="left:72px">
      <div class="feature-icon"><svg width="24" height="24" viewBox="0 0 24 24"><circle cx="12" cy="12" r="10" fill="none" stroke="#111" stroke-width="2"/><path d="M15.5 8.5a5 5 0 1 0 0 7" fill="none" stroke="#111" stroke-width="2"/></svg></div>
      <h3>Copyright Cateogries</h3>
      <p>Lorem Ipsum is simply dummy text of the printing and typesetting industry. Lorem Ipsum has been the indus-<br>try's standard</p>
    </div>
    <div class="abs feature" style="left:313px">
      <div class="feature-icon"><svg width="24" height="24" viewBox="0 0 24 24" fill="none" stroke="#111" stroke-width="1.6"><path d="M12 3v17M6 20h12M4 6h16"/><path d="M6 6l-3 7h6zM18 6l-3 7h6z"/></svg></div>
      <h3>Law &amp; Statutes</h3>
      <p>Lorem Ipsum is simply dummy text of the printing and typesetting industry. Lorem Ipsum has been the indus-<br>try's standard</p>
    </div>
    <div class="abs feature" style="left:553px">
      <div class="feature-icon"><svg width="24" height="24" viewBox="0 0 24 24"><path d="M3 5h18v11H10l-5 4v-4H3z" fill="#111"/><text x="12" y="13" font-family="Arial,sans-serif" font-size="5.5" fill="#fff" text-anchor="middle">FAQs</text></svg></div>
      <h3>FAQs</h3>
      <p>Lorem Ipsum is simply dummy text of the printing and typesetting industry. Lorem Ipsum has been the indus-<br>try's standard</p>
    </div>
  </section>

  <footer class="abs footer">
    <div class="abs footer-links"><span>ABOUT US</span><span>|</span><span>CUSTOMER SERVICE</span><span>|</span><span>PRIVACY POLICY</span><span>|</span><span>CONTACT US</span></div>
    <div class="abs footer-copy">© 2013 Rightsbloomery.com. All Rights Reserved.</div>
  </footer>

</div>
</body>
</html>
```